Business Cards and label design needed!

I am a metalsmith, working in sterling silver, brass and moving slowly into adding some gold accent pieces. I also use patinas to add color to brass pieces. The peacock feather is used in my packaging, as both a label and tissue paper. I am attaching what I am currently using, and printing at home, but I need a design that I can have professionally printed. My website is www.willowharborcrafts.com
Target Market(s)
Established Professionals, Independent thinkers, Art donors, Artist supporters
Industry/Entity Type
Jewelry
Contact Information for Business Card
I would like a business card with the basic contact information, including @willowharbor and @willowharbor. I currently use a peacock feather and would like to continue that. I like to use turquoise, Tiffany blue and colors in that direction. I am open to other suggestions. I would like to be able to transfer the design to oval labels as well.
Font styles to use
Other font styles liked:
- Garamond or other fonts that have a slight script that is easy to read
Look and feel

```html
<!DOCTYPE html>
<html lang="en">
<head>
<meta charset="utf-8">
<title>Willow Harbor Crafts – Business Card</title>
<link href="https://fonts.googleapis.com/css2?family=Fira+Sans:wght@400;500;600&display=swap" rel="stylesheet">
<style>
  :root {
    --backdrop: #a9a7a8;
    --mint: #c4ebe6;
    --paper: #ffffff;
    --navy: #1f3a7a;
    --teal: #3fa8a8;
    --rule: #dcdcdc;
    --band-mint: #b7e3d3;
    --band-navy: #213f86;
  }
  * { margin: 0; padding: 0; box-sizing: border-box; }
  html, body {
    width: 1200px; height: 1200px; overflow: hidden;
    background: var(--backdrop);
    font-family: "Fira Sans", Arial, sans-serif;
    color: var(--navy);
  }
  .canvas { position: relative; width: 1200px; height: 1200px; }
  .card {
    position: absolute; width: 712px; height: 419px;
    border-radius: 22px; overflow: hidden;
  }
  .card-front { left: 238px; top: 118px; background: var(--mint); }
  .card-back { left: 230px; top: 644px; background: var(--paper); }

  .brand-mark {
    position: absolute; border-radius: 50%; background: var(--teal);
  }
  .card-front .brand-mark { width: 34px; height: 34px; left: 339px; top: 120px; }
  .card-front .brand-name {
    position: absolute; left: 0; right: 0; top: 232px;
    text-align: center; font-size: 42px; font-weight: 500; letter-spacing: .5px;
  }
  .card-front .site {
    position: absolute; left: 0; right: 0; top: 379px;
    text-align: center; font-size: 16px;
  }

  .card-back .brand-mark { width: 30px; height: 30px; left: 500px; top: 60px; }
  .card-back .brand-name {
    position: absolute; right: 32px; top: 150px;
    font-size: 36px; font-weight: 500; letter-spacing: .5px;
  }
  .person-name {
    position: absolute; left: 36px; top: 226px;
    font-size: 26px; font-weight: 600;
  }
  .person-role {
    position: absolute; left: 36px; top: 262px; font-size: 15px;
  }
  .divider {
    position: absolute; left: 182px; top: 269px; width: 496px; height: 3px;
    background: var(--rule);
  }
  .contact-list {
    position: absolute; left: 374px; top: 302px; list-style: none;
    font-size: 17px; line-height: 24px;
  }
  .contact-list li { display: flex; align-items: center; }
  .contact-list svg { width: 16px; height: 16px; margin-right: 20px; fill: var(--navy); }
  .social {
    position: absolute; left: 36px; top: 343px; font-size: 16px;
    display: flex; gap: 10px; align-items: center;
  }
  .social .dot {
    width: 28px; height: 28px; border-radius: 50%; background: var(--navy);
  }
  .band { position: absolute; bottom: 0; left: 0; width: 712px; height: 17px; }
</style>
</head>
<body>
<main class="canvas">
  <section class="card card-front">
    <span class="brand-mark"></span>
    <h1 class="brand-name">Willow Harbor Crafts</h1>
    <p class="site">www.willowharborcrafts.com</p>
  </section>

  <section class="card card-back">
    <span class="brand-mark"></span>
    <h2 class="brand-name">Willow Harbor Crafts</h2>
    <p class="person-name">Maren Holt</p>
    <p class="person-role">Managing Director</p>
    <span class="divider"></span>
    <ul class="contact-list">
      <li><svg viewBox="0 0 16 16"><path d="M1 6c0-2 3-3 7-3s7 1 7 3v1h-4V5.5H5V7H1zM4 8h8l2 5H2z"/></svg>555.014.2290</li>
      <li><svg viewBox="0 0 16 16"><path d="M1 3h14v10H1zM2.5 4.5 8 9l5.5-4.5v7h-11z" fill-rule="evenodd"/></svg>studio@willowharborcrafts.com</li>
      <li><svg viewBox="0 0 16 16"><circle cx="8" cy="8" r="6.5" fill="none" stroke="#1f3a7a" stroke-width="1.5"/><path d="M1.5 8h13M8 1.5v13" stroke="#1f3a7a" stroke-width="1.2"/><ellipse cx="8" cy="8" rx="3" ry="6.5" fill="none" stroke="#1f3a7a" stroke-width="1.2"/></svg>www.willowharborcrafts.com</li>
    </ul>
    <p class="social">Follow us on: <span class="dot"></span><span class="handle">@willowharbor</span></p>
    <svg class="band" viewBox="0 0 712 17" preserveAspectRatio="none">
      <polygon points="0,0 360,0 352,17 0,17" fill="var(--band-mint)"/>
      <polygon points="360,0 712,0 712,17 352,17" fill="var(--band-navy)"/>
    </svg>
  </section>
</main>
</body>
</html>
```